Catalogue Design Project

we are college are would like have a,

College Hand out booklet, infomation book.

this book will be used for marketing,branding, given to new students, business, all information about our college including course information, college information, eg. a university ingo book A4 in size.
we would like to have the cover pages and all internal pages designed, then the content we can do locally.

Industry/Entity Type

University

```html
<!DOCTYPE html>
<html lang="en">
<head>
<meta charset="utf-8">
<title>Harwood College – Information Booklet</title>
<link href="https://fonts.googleapis.com/css2?family=Source+Sans+3:wght@400;600;700&display=swap" rel="stylesheet">
<style>
  :root {
    --backdrop: #808080;
    --paper: #ffffff;
    --brand-blue: #29a8e0;
    --brand-blue-light: #3bb2e6;
    --ink: #1a1a1a;
    --photo-warm: #b89a86;
    --photo-green: #4f7a4a;
    --photo-board: #3f6b52;
    --photo-city: #6f8a78;
    --photo-lawn: #7e9a5e;
  }
  * { box-sizing: border-box; margin: 0; padding: 0; }
  html, body { width: 755px; height: 1200px; overflow: hidden; }
  body {
    position: relative;
    background: var(--backdrop);
    font-family: "Source Sans 3", sans-serif;
    color: var(--ink);
  }
  .page, .cell, .tab, .copy { position: absolute; }
  .page { background: var(--paper); }

  /* Cover */
  .cover { left: 156px; top: 15px; width: 367px; height: 368px; }
  .cell { display: flex; align-items: center; justify-content: center; text-align: center; }
  .cell--blue { background: var(--brand-blue); color: var(--paper); }
  .cell--white { color: var(--brand-blue); }
  .photo { position: absolute; }
  .headline { font-size: 20px; font-weight: 400; line-height: 1.15; }
  .sub-headline { font-size: 14px; font-weight: 400; line-height: 1.2; }
  .brand-block {
    width: 121px; height: 87px; background: var(--brand-blue-light);
    display: flex; align-items: center; justify-content: center;
  }
  .brand-name { font-size: 10px; font-weight: 600; letter-spacing: 0.5px; color: var(--paper); }

  /* Spreads */
  .spread { left: 9px; width: 736px; height: 367px; }
  .spread--intro { top: 416px; }
  .spread--about { top: 806px; }

  .tab {
    top: 0; background: var(--brand-blue); color: var(--paper);
    font-size: 7.5px; font-weight: 700; letter-spacing: 0.2px;
    display: flex; align-items: center; justify-content: center;
  }
  .copy { font-size: 5.8px; line-height: 1.3; }
  .copy__title { color: var(--brand-blue); font-weight: 400; }
  .copy p + p { margin-top: 6px; }
</style>
</head>
<body>

  <!-- Cover page -->
  <section class="page cover">
    <div class="photo" role="img" aria-label="Photo of a smiling student holding a stack of books in front of library shelves"
         style="left:0;top:0;width:183px;height:185px;background:linear-gradient(135deg,#5a4a5e,var(--photo-warm) 55%,#d9cbbd);"></div>
    <div class="cell cell--white" style="left:183px;top:0;width:184px;height:185px;">
      <h1 class="headline">A Bright Future</h1>
    </div>
    <div class="cell cell--white" style="left:0;top:185px;width:183px;height:183px;">
      <p class="sub-headline">We get you ready</p>
    </div>
    <div class="cell cell--blue" style="left:183px;top:185px;width:184px;height:183px;">
      <div class="brand-block"><span class="brand-name">HARWOOD COLLEGE</span></div>
    </div>
  </section>

  <!-- Introduction spread -->
  <section class="page spread spread--intro">
    <div class="tab" style="left:13px;width:72px;height:52px;">Introduction</div>
    <div class="copy" style="left:40px;top:208px;width:278px;">
      <p><span class="copy__title">Why choose Harwood College?</span><br>
      Our mission at the Harwood College (HC) is to enable our students and staff to contribute to an effective learning environment in which they can aspire and achieve the goals, that rewards knowledge, excellence, commitment and extend our services to wider national and international communities.</p>
      <p>We focus on building strong relationship by sharing our resources and services with other education institutions, Universities, Government organizations and with the wider community in Australia and overseas.</p>
    </div>

    <div class="cell cell--blue" style="left:368px;top:0;width:183px;height:192px;">
      <h2 class="headline">Our Mission</h2>
    </div>
    <div class="photo" role="img" aria-label="Photo of a lecturer at a green chalkboard reading Philosophy, with students seated in front"
         style="left:551px;top:0;width:185px;height:192px;background:linear-gradient(160deg,var(--photo-board),#2e4f3e 60%,#2a2a2a);"></div>
    <div class="photo" role="img" aria-label="Photo of a smiling student in a striped shirt holding a yellow folder, classmates behind on a lawn"
         style="left:368px;top:192px;width:183px;height:175px;background:linear-gradient(180deg,var(--photo-green),#6e7f6a 60%,#2f3a55);"></div>
    <div class="cell cell--blue" style="left:551px;top:192px;width:185px;height:175px;">
      <h2 class="sub-headline">Effective learning<br>environment</h2>
    </div>
  </section>

  <!-- About spread -->
  <section class="page spread spread--about">
    <div class="photo" role="img" aria-label="Aerial photo of the city centre, river and stadium"
         style="left:0;top:0;width:368px;height:191px;background:linear-gradient(180deg,#8aa3ae,var(--photo-city) 35%,#5f7a5c);"></div>
    <div class="photo" role="img" aria-label="Photo of students studying together on the grass"
         style="left:0;top:191px;width:169px;height:176px;background:linear-gradient(160deg,#6b6a55,var(--photo-lawn) 55%,#c9c6b8);"></div>
    <div class="cell cell--blue" style="left:169px;top:191px;width:199px;height:176px;flex-direction:column;">
      <h2 class="headline">Heart of Brisbane</h2>
      <p class="sub-headline" style="font-size:13px;margin-top:4px;">Business District</p>
    </div>

    <div class="tab" style="left:640px;width:72px;height:42px;">About Us</div>
    <div class="copy" style="left:417px;top:196px;width:275px;">
      <p><span class="copy__title">About Harwood College</span><br>
      Harwood College is located at Woolloongabba, heart of Brisbane Business district which is easily accessible by bus, train, ferry and private transport. Woolloongabba is home to a world famous stadium known as “Riverside Stadium”. It is approximately 10 minutes walk from South bank of Brisbane River. Brisbane’s South Bank Parklands feature 17 hectares of lush gardens and lawns, and the magnificent Arbour. It has been awarded the best public sector development in the world by the Global Property Council and the world’s best downtown public space by the World City Centres Forum. There are restaurants, Cafes, Department stores and cinemas in the near surroundings of the College.</p>
    </div>
  </section>

</body>
</html>
```